Double Sided Business Card Design for Pet Services

My mom and I want to start a business for pets. We want to offer dog walking, pet sitting as well as boarding and grooming at our home. For the front of the business card, we want a logo that will capture all of our services. We want the name to be Morrito, Inc., which means little paws in Spanish. Perhaps, there could be little paws or just a little paw implemented within the word Morrito. Or we would want a cat and a dog by the word Morrito. We have a cat and a dog at home, and we would be really happy if they could be a part of the business card. It does not have to be anything crazy. Just an outline of a cat or a dog would be awesome. Please see uploaded file.
As for the back of the card, we would want little paws all over the card or we would want a collar, leash, grooming scissor, dog/cat bowl, bone, fish, or toy to show all of the services that we provide. Along with either the many paws or many pet objects, we would want to add our information, such as name (Rosalba Ferrin), telephone numbers (512) 876-2093, e-mail addresses morritoinc@bramwel.com, etc.
We would also want a catch phrase to go on the back of the card, such as "Where all paws matter!" Or "We strive for happy tails." or "A paw-bulous service is guaranteed!"
As for colors, we would not want that many. We would want perhaps white and blue. We would want soft colors that will stand out and make an impression. The same goes with the text. An elegant text would be nice. Or perhaps a text with bold letters. We are excited to see the results, but we are also excited to see your creative ideas and what you will bring to the table.

Target Market(s)

Pet Owners

Contact Information for Business Card

For the front of the business card, we want a logo that will capture all of our services. We want the name to be Morrito, Inc., which means little paws in Spanish. Perhaps, there could be little paws or just a little paw implemented within the word Morrito. Or we would want a cat and a dog by the word Morrito. We have a cat and a dog at home, and we would be really happy if they could be a part of the business card. It does not have to be anything crazy. Just an outline of a cat or a dog would be awesome. Please see uploaded file.
As for the back of the card, we would want little paws all over the card or we would want a collar, leash, grooming scissor, dog/cat bowl, bone, fish, or toy to show all of the services that we provide. Along with either the many paws or many pet objects, we would want to add our information, such as name, telephone numbers, e-mail addresses, etc. We would also want a catch phrase to go on the back of the card, such as "Where all paws matter!" Or "We strive happy tails." or "A paw-bulous service is guaranteed!" Or if there is a way to put the catch phrase in the front of the card. We are open to seeing variety.

Logo Text

Morrito, Inc

Font styles to use
Serif
Script

Colors
ffffff
33a6d7
145ea8

Requirements
Must have
• My project must be a double sided business card.

```html
<!DOCTYPE html>
<html lang="en">
<head>
<meta charset="utf-8">
<title>Morrito, Inc. — Business Card</title>
<link rel="stylesheet" href="https://fonts.googleapis.com/css2?family=Kaushan+Script&family=Noto+Serif:wght@700&family=Open+Sans:wght@400&family=Arimo:wght@400&display=swap">
<style>
  :root {
    --backdrop: #1c1c1e;
    --back-blue: #2fa3d8;
    --back-band: #2b98cc;
    --pattern-tone: #2a8fc2;
    --front-blue: #3b98d4;
    --deep-blue: #145ea8;
    --white: #ffffff;
    --ink: #0d0d0d;
  }
  * { box-sizing: border-box; margin: 0; padding: 0; }
  html, body { width: 1200px; height: 1200px; overflow: hidden; background: var(--backdrop); }
  .sheet { position: relative; width: 1200px; height: 1200px; }

  .card {
    position: absolute; left: 150px; width: 900px; height: 514px;
    overflow: hidden; box-shadow: 0 10px 30px rgba(0,0,0,.5);
  }

  /* Back side */
  .card--back { top: 60px; background: var(--back-blue); }
  .back-pattern {
    position: absolute; inset: 0;
    background:
      radial-gradient(circle at 30% 30%, rgba(20,94,168,.18), transparent 60%),
      radial-gradient(circle at 75% 70%, rgba(20,94,168,.16), transparent 55%),
      var(--back-blue);
  }
  .back-band {
    position: absolute; left: 0; top: 0; bottom: 0; width: 92px;
    background: var(--back-band);
    box-shadow: 14px 0 22px rgba(0,0,0,.28);
  }
  .band-icon { position: absolute; left: 28px; width: 36px; height: 36px; }
  .band-icon--phone { top: 232px; }
  .band-icon--mail { top: 318px; }
  .back-name {
    position: absolute; left: 160px; top: 40px;
    font: 64px "Kaushan Script", cursive; color: var(--white);
  }
  .back-contact {
    position: absolute; left: 160px; color: var(--white);
    font: 30px "Open Sans", sans-serif;
  }
  .back-contact--phone { top: 228px; }
  .back-contact--email { top: 316px; }
  .back-slogan {
    position: absolute; left: 150px; bottom: 40px;
    font: 70px "Kaushan Script", cursive; color: var(--white);
  }

  /* Front side */
  .card--front { top: 626px; background: var(--front-blue); }
  .front-tagline {
    position: absolute; left: 80px; top: 120px;
    font: italic 17px "Arimo", sans-serif; color: var(--ink);
  }
  .front-art {
    position: absolute; right: 60px; top: 40px; width: 300px; height: 420px;
    border-radius: 45% 45% 30% 30%;
    background: radial-gradient(ellipse at 50% 50%, rgba(255,255,255,.16), rgba(255,255,255,0) 70%);
  }
  .brand { position: absolute; left: 70px; top: 260px; display: flex; align-items: center; gap: 22px; }
  .brand-dot { width: 70px; height: 70px; border-radius: 50%; background: var(--white); }
  .brand-name { font: 700 84px "Noto Serif", serif; color: var(--ink); line-height: 1; }
  .brand-sub {
    position: absolute; left: 420px; top: 366px;
    font: 36px "Arimo", sans-serif; color: var(--white);
  }
</style>
</head>
<body>
<div class="sheet">

  <section class="card card--back" aria-label="Card back">
    <div class="back-pattern" role="img" aria-label="Scattered pattern of paw prints, bones, fish skeletons and pet food bowls"></div>
    <div class="back-band">
      <svg class="band-icon band-icon--phone" viewBox="0 0 24 24" aria-hidden="true">
        <path fill="#fff" d="M6.6 10.8a15 15 0 0 0 6.6 6.6l2.2-2.2a1 1 0 0 1 1-.25 11.4 11.4 0 0 0 3.6.6 1 1 0 0 1 1 1V20a1 1 0 0 1-1 1A17 17 0 0 1 3 4a1 1 0 0 1 1-1h3.5a1 1 0 0 1 1 1c0 1.25.2 2.45.6 3.6a1 1 0 0 1-.25 1z"/>
      </svg>
      <svg class="band-icon band-icon--mail" viewBox="0 0 24 24" aria-hidden="true">
        <rect x="2" y="5" width="20" height="14" fill="#fff"/>
        <path d="M2 5l10 8 10-8M2 19l7-7M22 19l-7-7" stroke="#2b98cc" stroke-width="1.5" fill="none"/>
      </svg>
    </div>
    <h1 class="back-name">Rosalba Ferrin</h1>
    <p class="back-contact back-contact--phone">+512 876 2093</p>
    <p class="back-contact back-contact--email">morritoinc@bramwel.com</p>
    <p class="back-slogan">Where all paws matter!</p>
  </section>

  <section class="card card--front" aria-label="Card front">
    <p class="front-tagline">“A paw-bulous service is guaranteed”</p>
    <div class="front-art" role="img" aria-label="White line outline of a dog and a cat sitting side by side"></div>
    <div class="brand">
      <span class="brand-dot"></span>
      <span class="brand-name">Morrito, Inc.</span>
    </div>
    <p class="brand-sub">Pet Services</p>
  </section>

</div>
</body>
</html>
```